Website Design for Spatial Humanities Non-Profit: Civic Landmark Atlas

We seek a Wordpress website template for Civic Landmark Atlas (CLA) a 501(c)(3) non-profit in the emergent field of spatial humanities dedicated to digitally preserving global historic and cultural sites. A unique collaboration between individuals in diverse disciplines (academia, technology, arts, and social entrepreneurship), CLA melds age-old scholarship with 21st Century technology to assert the importance of physical location to the understanding of history. This actualized focus allows for a more comprehensive, interactive, and “living” reconstruction of the past than previously thought possible.
CLA, through its own initiatives as well as those of others to whom it provides services, has created a prototype for digital preservation applicable to every country, culture, and subject matter. The organization is
• Pioneering new technology and multimedia techniques for documenting historic and cultural sites;
• Leading international field expeditions to geo-locate and digitize sites, as well as record eyewitness testimony; and
• Transforming research data into dynamically new educational applications.
The template should have a distinctive homepage, themed pages (about, news, projects, opportunities), and no blog elements (e.g., comment section). Admin friendliness is a plus.
We have posted separately for a logo design, which will perhaps feature a scattering of pixels horizontally that gradually cohere to form a globe (featuring "CLA") in the center. To participate in that contest see: http://gigs.pixelvaultwork.com/gig.aspx?id=48213
Non-Profit

```html
<!DOCTYPE html>
<html lang="en">
<head>
<meta charset="utf-8">
<title>Civic Landmark Atlas</title>
<link href="https://fonts.googleapis.com/css2?family=Arimo:wght@400;700&family=Questrial&display=swap" rel="stylesheet">
<style>
:root{
  --blue-deep:#0a3f8f;
  --blue-mid:#1668c0;
  --blue-light:#3aa6e8;
  --accent:#2a86c8;
  --panel:#ffffff;
  --page:#ececec;
  --text:#666666;
  --head:#222222;
  --news-bg:#f3f3f3;
  --footer:#0b3f86;
  --footer-text:#5bb8ee;
  --nav-active:#0c4a8a;
}
*{margin:0;padding:0;box-sizing:border-box}
html,body{width:818px;height:1200px;overflow:hidden}
body{position:relative;background:var(--page);font-family:Arimo,Arial,sans-serif;color:var(--text)}
.abs{position:absolute}
.header-band{left:0;top:0;width:818px;height:260px;background:linear-gradient(180deg,#0f5fb5 0%,#1a76cc 45%,#0c4f9f 100%)}
.brand{left:104px;top:20px;display:flex;align-items:center;gap:8px}
.brand-mark{width:76px;height:76px;border-radius:50%;background:#3aa0e6}
.brand-name{color:#fff;font-size:46px;font-weight:700;line-height:1}
.brand-sub{color:#fff;font-size:10px;font-weight:700;margin-top:2px;white-space:nowrap}
.top-links{left:634px;top:14px;color:#fff;font-size:8.5px;white-space:nowrap}
.top-links .sep{margin:0 9px}
.nav-item{top:45px;height:20px;line-height:20px;font-size:8px;font-weight:700;color:#fff;text-decoration:none;white-space:nowrap}
.nav-item.active{left:392px;width:57px;text-align:center;background:var(--nav-active);border-radius:3px}
.panel{left:95px;top:98px;width:627px;height:922px;background:var(--panel)}
.hero{left:105px;top:108px;width:608px;height:254px;background:linear-gradient(120deg,#cfe3ee 0%,#9fc6dc 50%,#e6f0f4 100%)}
.welcome{left:104px;top:376px;font-family:Questrial,sans-serif;font-weight:400;font-size:26px;color:#999;white-space:nowrap}
.welcome span{color:var(--accent)}
.intro{left:104px;width:610px;font-size:8.2px;line-height:15.5px;color:#666}
.divider{left:104px;top:536px;width:609px;height:3px;background:#f0f0f0}
.sec-title{font-size:12px;font-weight:700;color:var(--head);display:flex;align-items:center;gap:8px;white-space:nowrap}
.sec-icon{width:18px;height:18px;border-radius:3px;background:#c9d9c0}
.news{left:104px;top:588px;width:214px;height:257px;background:var(--news-bg)}
.news-item{position:absolute;left:0;width:214px;height:81px;border-bottom:1px solid #e4e4e4}
.cal{position:absolute;left:11px;top:16px;width:38px;height:36px;background:#fff;border:1px solid #ccc;border-radius:3px;text-align:center;font-weight:700}
.cal b{display:block;background:#777;color:#fff;font-size:6px;height:11px;line-height:11px}
.cal i{font-style:normal;font-size:13px;color:#333;line-height:22px}
.news-title{position:absolute;left:59px;top:16px;font-size:9px;color:var(--accent);white-space:nowrap}
.news-body{position:absolute;left:59px;top:32px;width:148px;font-size:7.6px;line-height:12px;color:#555}
.tab{width:30px;height:10px;background:#29a3e6;border-radius:2px}
.map{left:343px;top:588px;width:370px;height:255px;background:#f4f4f4;padding:5px}
.map div{width:100%;height:100%;background:linear-gradient(135deg,#ece6d8,#dcd6c6)}
.carousel{left:105px;top:893px;width:608px;height:117px;background:linear-gradient(#f8f8f8,#e6e6e6);border:1px solid #ddd;border-radius:4px}
.arrow{top:0;width:25px;height:115px;background:#d2d2d2}
.thumb{top:16px;width:116px;height:84px;background:#fff;padding:3px;box-shadow:0 1px 3px rgba(0,0,0,.25)}
.thumb div{width:100%;height:100%}
.footer{left:0;top:1043px;width:818px;height:157px;background:linear-gradient(180deg,#0a3a80,#0e4f9a)}
.fcol{top:1060px;width:180px}
.fhead{color:#fff;font-size:10.5px;margin-bottom:8px;white-space:nowrap}
.ftext{color:var(--footer-text);font-size:8px;line-height:14px}
.vline{top:1055px;width:1px;height:145px;background:#0a3570}
.input{width:140px;height:18px;border-radius:9px;background:#06305f;color:#4a7fb5;font-size:8px;line-height:18px;padding-left:8px;margin-top:16px}
.contact-row{display:flex;white-space:nowrap}.contact-row span:first-child{width:47px}
.white{color:#fff}
.feed{display:flex;gap:12px;margin-bottom:14px;white-space:nowrap}
.feed-dot{width:20px;height:20px;border-radius:50%;background:#4a9ad8;flex:none;margin-top:4px}
.social{display:flex;gap:3px;margin-top:4px}.social i{width:12px;height:12px;background:#244f86;border-radius:2px}
</style>
</head>
<body>
<div class="abs header-band"></div>
<div class="abs brand">
  <div class="brand-mark"></div>
  <div><div class="brand-name">CLA</div><div class="brand-sub">Civic Landmark Atlas, Inc.</div></div>
</div>
<div class="abs top-links">HOME<span class="sep">|</span>CONTACT</div>
<nav>
  <a class="abs nav-item active">ABOUT US</a>
  <a class="abs nav-item" style="left:479px">LATEST NEWS</a>
  <a class="abs nav-item" style="left:571px">PROJECTS</a>
  <a class="abs nav-item" style="left:650px">OPPORTUNITIES</a>
</nav>

<div class="abs panel"></div>
<div class="abs hero" role="img" aria-label="Photo of a woman in safety glasses touching a transparent digital interface"></div>
<h1 class="abs welcome">Welcome to <span>Civic Landmark Atlas Inc.</span></h1>
<p class="abs intro" style="top:410px">Lorem Ipsum is simply dummy text of the printing and typesetting industry. Lorem Ipsum has been the industry's standard dummy text ever since the 1500s, when an unknown printer took a galley of type and scrambled it to make a type specimen book. It has survived not only five centuries, but also the leap into electronic typesetting, remaining essentially unchanged.</p>
<p class="abs intro" style="top:472px">Lorem Ipsum is simply dummy text of the printing and typesetting industry. Lorem Ipsum has been the industry's standard dummy text ever since the 1500s, when an unknown printer took a galley of type and scrambled it to make a type specimen book. It has survived not only five centuries, but also the leap into electronic typesetting, remaining essentially unchanged.</p>
<div class="abs divider"></div>

<h2 class="abs sec-title" style="left:104px;top:553px">Latest News <span class="sec-icon"></span></h2>
<h2 class="abs sec-title" style="left:336px;top:553px">Our Location <span class="sec-icon" style="background:#e8c86a"></span></h2>

<div class="abs news">
  <div class="news-item" style="top:6px"><div class="cal"><b>AUG</b><i>21</i></div><div class="news-title">Lorem Ipsum is simply dummy text.</div><div class="news-body">Lorem Ipsum is simply dummy text of the printing and typesetting industry. Lorem Ipsum has been the industry's standard dummy text ever since the 1500s.</div></div>
  <div class="news-item" style="top:87px"><div class="cal"><b>AUG</b><i>21</i></div><div class="news-title">Lorem Ipsum is simply dummy text.</div><div class="news-body">Lorem Ipsum is simply dummy text of the printing and typesetting industry. Lorem Ipsum has been the industry's standard dummy text ever since the 1500s.</div></div>
  <div class="news-item" style="top:168px;border:0"><div class="cal"><b>AUG</b><i>21</i></div><div class="news-title">Lorem Ipsum is simply dummy text.</div><div class="news-body">Lorem Ipsum is simply dummy text of the printing and typesetting industry. Lorem Ipsum has been the industry's standard dummy text ever since the 1500s.</div></div>
</div>
<div class="abs tab" style="left:198px;top:584px"><svg width="30" height="10"><path d="M12 7l3-3 3 3z" fill="#fff"/></svg></div>
<div class="abs tab" style="left:198px;top:838px"><svg width="30" height="10"><path d="M12 3l3 3 3-3z" fill="#fff"/></svg></div>

<div class="abs map"><div role="img" aria-label="Street map of the organisation's city location"></div></div>

<h2 class="abs sec-title" style="left:105px;top:868px">Our Recent Projects <span class="sec-icon" style="background:#9fc0e0"></span></h2>
<div class="abs carousel">
  <div class="abs arrow" style="left:0"><svg width="25" height="115"><path d="M16 48l-7 10 7 10" stroke="#fff" stroke-width="3" fill="none"/></svg></div>
  <div class="abs arrow" style="right:0"><svg width="25" height="115"><path d="M9 48l7 10-7 10" stroke="#fff" stroke-width="3" fill="none"/></svg></div>
  <div class="abs thumb" style="left:42px"><div role="img" aria-label="Project photo of office staff" style="background:linear-gradient(135deg,#cfd3d6,#a03a3a)"></div></div>
  <div class="abs thumb" style="left:178px"><div role="img" aria-label="Project photo of a team meeting" style="background:linear-gradient(135deg,#bcd2dc,#5c7a8c)"></div></div>
  <div class="abs thumb" style="left:314px"><div role="img" aria-label="Project photo of seniors at a table" style="background:linear-gradient(135deg,#c9b59a,#7d5a48)"></div></div>
  <div class="abs thumb" style="left:449px"><div role="img" aria-label="Project photo of colleagues working together" style="background:linear-gradient(135deg,#d8d8cf,#5f8a3a)"></div></div>
</div>

<div class="abs footer"></div>
<div class="abs vline" style="left:275px"></div>
<div class="abs vline" style="left:494px"></div>
<div class="abs fcol" style="left:95px;width:155px">
  <div class="fhead">Newsletter Sign up</div>
  <div class="ftext">Users avoid filling out forms and submitting their details if possible. For a newsletter sign-ups, all you need is their email address.</div>
  <div class="input">Enter Email</div>
  <div class="ftext white" style="margin-top:6px;margin-left:3px">Sign Up »</div>
</div>
<div class="abs fcol" style="left:314px">
  <div class="fhead">Contact Details</div>
  <div class="ftext">
    <div class="contact-row"><span>Company:</span><span>Lorem Ipsum.</span></div>
    <div class="contact-row"><span>Street:</span><span>Lorem Ipsum is dummy text</span></div>
    <div class="contact-row"><span>Postal/City:</span><span>000123, City Name</span></div>
    <div class="contact-row"><span>Email:</span><span class="white">info@civicatlas-mail.org</span></div>
    <div class="contact-row"><span>Phone:</span><span>000 123, 4567</span></div>
  </div>
  <div class="fhead" style="margin-top:12px;margin-bottom:2px">Social Links</div>
  <div class="social"><i></i><i></i><i></i><i></i></div>
</div>
<div class="abs fcol" style="left:533px">
  <div class="fhead">Chatter Feed</div>
  <div class="feed"><span class="feed-dot"></span><div class="ftext">Featured Workspace: Mystery Author #2<br><span class="white">http://lnk.cl/aR7qLm</span><br>1 hours ago</div></div>
  <div class="feed"><span class="feed-dot"></span><div class="ftext">Featured Workspace: Mystery Author #2<br><span class="white">http://lnk.cl/aR7qLm</span><br>1 hours ago</div></div>
</div>
</body>
</html>
```